Dialysis Brochure

12 pages booklet, horizontal, 9 inches width x 6 inches high , luxury look
Updates

Landscape booklet 9 x 6

Need extra days to review

Target Market(s)

General public

Industry/Entity Type

Health Care

Colors

Designer to choose colors to be used in the design.

Requirements
Nice to have
• foil effect or similar

```html
<!DOCTYPE html>
<html lang="en">
<head>
<meta charset="utf-8">
<title>Dialysis Brochure – 2018 Data Spread</title>
<link rel="stylesheet" href="https://fonts.googleapis.com/css2?family=Source+Sans+3:wght@300;400;600;700&display=swap">
<style>
  :root {
    --panel: #e4e2de;
    --ink: #262626;
    --muted: #55524e;
    --band: rgba(101, 88, 78, 0.93);
    --band-text: #f4f0eb;
    --rule: #cfc6bd;
    --ceiling-light: #f3f4f5;
    --ceiling: #d9dcdf;
    --wall: #c7c9cb;
    --wood: #b98f63;
    --wood-soft: #cdb494;
    --floor: #a9acaf;
    --floor-dark: #8f9295;
  }
  * { box-sizing: border-box; margin: 0; padding: 0; }
  html, body { width: 1200px; height: 400px; overflow: hidden; background: var(--panel); }
  body { font-family: "Source Sans 3", "Myriad Pro", Arial, sans-serif; color: var(--ink); }

  .spread { position: relative; width: 1200px; height: 400px; }

  .clinic-photo {
    position: absolute; left: 0; top: 0; width: 844px; height: 400px;
    background:
      radial-gradient(ellipse 260px 120px at 420px 40px, rgba(255,255,255,.75), rgba(255,255,255,0) 70%),
      radial-gradient(ellipse 420px 70px at 400px 195px, rgba(214,190,158,.55), rgba(214,190,158,0) 75%),
      linear-gradient(180deg,
        var(--ceiling-light) 0%,
        var(--ceiling) 22%,
        #e6e7e8 34%,
        var(--wall) 42%,
        var(--wood-soft) 47%,
        var(--wood) 51%,
        #c3a27d 55%,
        #b8babc 60%,
        var(--floor) 72%,
        var(--floor-dark) 100%);
  }

  .highlights {
    position: absolute; left: 0; top: 305px; width: 844px; height: 60px;
    background: var(--band); color: var(--band-text);
  }
  .highlight { position: absolute; top: 7px; font-size: 7.4px; line-height: 11.1px; white-space: nowrap; }
  .highlight h3 { font-size: 7.4px; font-weight: 700; line-height: 11.1px; letter-spacing: .1px; }
  .highlight--survival { left: 55px; }
  .highlight--rating { left: 236px; }
  .highlight--safety { left: 424px; }
  .highlight-divider { position: absolute; top: 8px; width: 1px; height: 45px; background: var(--rule); }
  .highlight-divider--one { left: 227px; }
  .highlight-divider--two { left: 415px; }

  .data-panel { position: absolute; left: 844px; top: 0; width: 356px; height: 400px; background: var(--panel); }
  .data-title {
    position: absolute; left: 58px; top: 56px;
    font-size: 24px; font-weight: 300; letter-spacing: 3.4px; color: #3a3835; line-height: 30px;
  }
  .data-table {
    position: absolute; left: 59px; top: 89px; width: 238px;
    border-collapse: collapse; background: #fff; font-size: 6.6px; line-height: 8.8px; table-layout: fixed;
  }
  .data-table th, .data-table td {
    border: 0.6px solid #222; vertical-align: top; text-align: left; padding: 0 2px 0 12px; overflow: hidden;
  }
  .data-table th { font-weight: 700; height: 9px; line-height: 8.6px; }
  .data-table td small { font-size: 5.1px; line-height: 7.3px; }
  .data-table .label small { display: block; }
  .data-table .num { padding-left: 19px; }
  .data-table .verdict { padding-left: 12px; }
  .data-table .nat { padding-left: 13px; }
  .data-table .center { text-align: center; padding-left: 2px; }
  .data-table .stars { display: block; font-size: 10px; line-height: 10px; letter-spacing: -0.6px; }
  .data-table .head-nyc { padding-left: 3px; }
  .col-ind { width: 71px; } .col-nyc { width: 56px; } .col-verdict { width: 51px; } .col-nat { width: 60px; }
  .r1 td { height: 25px; } .r2 td { height: 32px; } .r3 td { height: 26px; }
  .r4 td { height: 32px; } .r5 td { height: 33px; } .r6 td { height: 27px; }

  .summary { position: absolute; left: 59px; top: 282px; font-size: 7.6px; line-height: 11.1px; color: var(--muted); white-space: nowrap; }
  .summary ul { list-style: none; }
  .summary li { padding-left: 7px; position: relative; }
  .summary li::before { content: "•"; position: absolute; left: 0; }
</style>
</head>
<body>
<div class="spread">
  <div class="clinic-photo" role="img" aria-label="Photograph of a bright modern dialysis treatment floor with patients in reclining chairs, wood-panelled nurse stations and staff at work"></div>

  <div class="highlights">
    <div class="highlight highlight--survival">
      <h3>PATIENT SURVIVAL RATE:</h3>
      <p>RBKC had the Lowest Mortality Rate (higher survival)<br>in New York State for 2011-2017 years – 11.7 (per 100<br>patients)</p>
    </div>
    <span class="highlight-divider highlight-divider--one"></span>
    <div class="highlight highlight--rating">
      <h3>NATIONAL CARE RATING:</h3>
      <p>RBKC received 5-Star rating 9 times out of the last 10<br>years. Only 15% of Dialysis Centers in the United States<br>receive 5-Star rating in any particular year</p>
    </div>
    <span class="highlight-divider highlight-divider--two"></span>
    <div class="highlight highlight--safety">
      <h3>PATIENT SAFETY PROGRAM:</h3>
      <p>5-Diamond Award – 2016, 2017, 2018. Every<br>single year starting 2016 when this program<br>was established</p>
    </div>
  </div>

  <section class="data-panel">
    <h2 class="data-title">2018 DATA</h2>
    <table class="data-table">
      <colgroup><col class="col-ind"><col class="col-nyc"><col class="col-verdict"><col class="col-nat"></colgroup>
      <tr><th>Indicators</th><th colspan="2" class="head-nyc">RBKC</th><th class="nat">Nationwide</th></tr>
      <tr class="r1"><td class="label">Quality of Care<small>/National Care Star<br>Rating/</small></td><td class="center">5-Star<span class="stars">★★★★★</span></td><td class="verdict">Excellent</td><td class="nat">Average 3-4</td></tr>
      <tr class="r2"><td class="label">Mortality Rate<small>(per 100 patients.<br>Lower number is<br>better)</small></td><td class="num" style="padding-top:9px">12.7</td><td class="verdict">Better<br>than<br>expected</td><td class="nat">17.4</td></tr>
      <tr class="r3"><td class="label">Infection Rate<small>(lower number is<br>better)</small></td><td class="num">0.24</td><td class="verdict">Better<br>than<br>expected</td><td class="nat">1.01</td></tr>
      <tr class="r4"><td>Blood<br>Transfusions <small>(per</small><br><small>100 patients. Lower<br>number is better)</small></td><td class="num">11.8</td><td class="verdict">Better<br>than<br>expected</td><td class="nat">39.2</td></tr>
      <tr class="r5"><td class="label">Blood waste<br>removal Rate<small>(higher number is<br>better)</small></td><td class="num">96.3%</td><td class="verdict">As<br>expected</td><td class="nat">95.9%</td></tr>
      <tr class="r6"><td>Hospitalizations<br>Rate <small>(lower</small><br><small>number is better)</small></td><td class="num">161.2</td><td class="verdict">Better<br>than<br>expected</td><td class="nat">183.2</td></tr>
    </table>

    <div class="summary">
      <p>Over the last ten years RBKC outperformed every other dialysis facility in the area:</p>
      <ul>
        <li>Higher survival rate for our patients</li>
        <li>The lower infection incidents rate</li>
        <li>The most efficiency of removal waste from blood</li>
        <li>The higher patient satisfaction rate</li>
      </ul>
    </div>
  </section>
</div>
</body>
</html>
```